Buchcover-Design für Ratgeber
Zielgruppe
Wir veröffentlichen Ebooks und Taschenbücher auf Lumora und benötigen für ein aktuelles Projekt noch ein Ebook Cover. Die Zielgruppe sind werdende und frisch gebackene Väter im Alter zwischen 25 und 40 Jahren.
Titel: KNIRPSOLOGIE, Vati kriegt das hin
Untertitel: Raus aus der Panik und rein ins Vater werden mit Verantwortung, Herz und Stil
Autor: Gernot Wallbrecht
Der Fokus des Buches richtet sich darauf, Vätern und denen, die es noch werden wollen, wertvolle Tipps und Handlungsempfehlungen mitzugeben, wie man sich als moderner, engagiertet Vater positioniert. Es richtet sich an Männer, die sich aktiv in die Erziehung ihres Kindes einbringen wollen und mehr sein wollen, als nur der Ernährer und Geldverdiener. Diese Zielgruppe ist bereit, Zeit zu investieren und sich darum zu bemühen, sich das Wissen anzueignen, wie sie ihre Partnerin während Schwangerschaft und Geburt unterstützen und wie sie eine starke Vater-Kind-Beziehung aufbauen können.
Das Hauptproblem dieser Zielgruppe ist, dass sie nur wenig Ahnung von Kindererziehung oder Schwangerschaft hat. Daher herrscht hier eine große Ratlosigkeit und Unsicherheit vor, da sie zum einen möglichst alles richtig machen will, zum Anderen aber nicht weiß, wie sie das anstellen und worauf alles zu achten ist.
Das Buch soll mit Cover und Titel die Botschaft senden, dass diese Sorgen unnötig sind und dass Daddy schon alles regelt. natürlich nur, wenn er das Buch gelesen hat ;-)
Aufgabenstellung
Wir hätten gerne ein Cover, welches ein kreatives Konzept abbildet und nicht nach Quobix-Standard bloß Titel, Stockfoto und den Namen des Autors darstellt. Ich denke es eignet sich hier mit dem Titel etwas auszuprobieren, da so ein Wortspiel wahrscheinlich einiges an kreativen Möglichkeiten bietet. Grundsätzlich sollten Cover, Titel und Untertitel miteinander harmonieren und ein schlüssiges Konzept darstellen, welches die Botschaft des Buches einfach rüber bringt.
Ansonsten haben wir keine weiteren Angaben wie Farben, Beispielcover usw. Hier könnt ihr kreativ werden!

```html
<!DOCTYPE html>
<html lang="de">
<head>
<meta charset="utf-8">
<title>KNIRPSOLOGIE – Buchcover</title>
<link rel="stylesheet" href="https://fonts.googleapis.com/css2?family=Didact+Gothic&family=Delius&family=Mr+Dafoe&display=swap">
<style>
  :root {
    --sky: #96bcd6;
    --navy: #1b3356;
    --navy-band: rgba(34, 52, 94, 0.88);
    --red: #c1181c;
    --white: #ffffff;
    --bubble: #f4f6fa;
  }
  html, body { margin: 0; padding: 0; overflow: hidden; }
  body { width: 1200px; height: 841px; background: var(--sky); font-family: "Didact Gothic", sans-serif; }
  .cover-spread { position: relative; width: 1200px; height: 841px; overflow: hidden; }

  /* Back cover */
  .back-cover { position: absolute; left: 0; top: 0; width: 557px; height: 841px; background: var(--sky); }
  .blurb-panel { position: absolute; left: 103px; top: 99px; width: 345px; height: 579px; background: var(--navy); }
  .author-portrait {
    position: absolute; left: 22px; top: 76px; width: 189px; height: 231px;
    background: radial-gradient(circle at 48% 42%, #c79a86 0%, #9a7a6c 30%, #5c6470 62%, #e4e6e4 100%);
  }
  .blurb {
    position: absolute; color: var(--white); font-size: 12.6px; line-height: 16.7px;
    margin: 0; text-align: justify; hyphens: manual;
  }
  .blurb--lead { left: 226px; top: 137px; width: 188px; }
  .blurb--audience { left: 139px; top: 338px; width: 276px; }
  .blurb--problem { left: 139px; top: 438px; width: 276px; }
  .author-signature {
    position: absolute; left: 232px; top: 596px; width: 196px; text-align: right;
    font-family: "Mr Dafoe", cursive; font-size: 28px; color: var(--white);
  }

  /* Spine */
  .spine { position: absolute; left: 557px; top: 0; width: 89px; height: 841px; background: var(--navy); }
  .spine-title {
    position: absolute; left: 50%; top: 50%; width: 800px;
    transform: translate(-50%, -50%) rotate(-90deg);
    display: flex; align-items: baseline; justify-content: center; gap: 18px;
    font-family: "Delius", sans-serif; white-space: nowrap;
  }
  .spine-title__main { color: var(--white); font-size: 46px; }
  .spine-title__claim { color: var(--red); font-size: 36px; }

  /* Front cover */
  .front-cover { position: absolute; left: 646px; top: 0; width: 554px; height: 841px; overflow: hidden; }
  .cover-photo {
    position: absolute; inset: 0;
    background:
      radial-gradient(ellipse 38% 30% at 36% 40%, #e7b59c 0%, #d3a08a 45%, rgba(211,160,138,0) 100%),
      radial-gradient(ellipse 45% 35% at 30% 20%, #8c97ab 0%, rgba(140,151,171,0) 100%),
      linear-gradient(170deg, #6d85a8 0%, #a9a2a0 45%, #5f5147 75%, #2f3c5c 100%);
  }
  .speech-bubbles { position: absolute; inset: 0; }
  .subtitle-band {
    position: absolute; left: 139px; top: 738px; width: 415px; height: 57px;
    background: var(--navy-band); color: var(--white);
    font-size: 18.5px; line-height: 23px; text-align: right;
    box-sizing: border-box; padding: 7px 12px 0 0; margin: 0;
  }
  .author-name {
    position: absolute; right: 12px; top: 808px; margin: 0;
    color: var(--white); font-size: 18px;
  }
</style>
</head>
<body>
<main class="cover-spread">

  <section class="back-cover">
    <div class="blurb-panel"></div>
    <div class="author-portrait" role="img" aria-label="Porträtfoto des Autors im grauen Rollkragenpullover"></div>
    <p class="blurb blurb--lead">Der Fokus des Buches richtet sich darauf, Vätern und denen, die es noch werden wollen, wertvolle Tipps und Handlungsempfehlun&shy;gen mitzugeben, wie man sich als moderner, engagiertet Vater posi&shy;tioniert. Es richtet sich an Männer, die sich aktiv in die Erziehung ihres Kindes einbringen wollen und mehr sein wollen, als nur der Ernährer und Geldverdienner.</p>
    <p class="blurb blurb--audience">Diese Zielgruppe ist bereit, Zeit zu investieren und sich darum zu bemühen, sich das Wissen anzueig&shy;nen, wie sie ihre Partnerin während Schwanger&shy;schaft und Geburt unterstützen und wie sie eine starke Vater-Kind-Beziehung aufbauen können.</p>
    <p class="blurb blurb--problem">Das Hauptproblem dieser Zielgruppe ist, dass sie nur wenig Ahnung von Kindererziehung oder Schwangerschaft hat. Daher herrscht hier eine große Ratlosigkeit und Unsicherheit vor, da sie zum einen möglichst alles richtig machen will, zum Anderen aber nicht weiß, wie sie das anstellen und worauf alles zu achten ist.</p>
    <div class="author-signature">Gernot Wallbrecht</div>
  </section>

  <section class="spine">
    <div class="spine-title">
      <span class="spine-title__main">KNIRPSOLOGIE</span>
      <span class="spine-title__claim">Vati kriegt das hin!</span>
    </div>
  </section>

  <section class="front-cover">
    <div class="cover-photo" role="img" aria-label="Foto: Baby mit blauer Fleecemütze hält die Hand des Vaters"></div>

    <svg class="speech-bubbles" width="554" height="841" viewBox="0 0 554 841" aria-hidden="false">
      <g class="bubble bubble--claim" transform="rotate(-15 357 145)">
        <path d="M212 40 H500 Q530 40 530 70 V205 Q530 235 500 235 H470 L488 280 L430 235 H212 Q182 235 182 205 V70 Q182 40 212 40 Z"
              fill="var(--bubble)" fill-opacity="0.93" stroke="var(--navy)" stroke-width="5" stroke-linejoin="round"/>
        <text x="356" y="108" text-anchor="middle" font-family="Delius, sans-serif" font-size="44" fill="var(--navy)">…OLOGIE</text>
        <text x="356" y="160" text-anchor="middle" font-family="Delius, sans-serif" font-size="32" fill="var(--red)">Vati kriegt</text>
        <text x="356" y="200" text-anchor="middle" font-family="Delius, sans-serif" font-size="32" fill="var(--red)">das hin!</text>
      </g>
      <g class="bubble bubble--knirps" transform="rotate(-15 250 530)">
        <path d="M140 455 H220 L245 410 L262 455 H355 Q385 455 385 485 V580 Q385 610 355 610 H140 Q110 610 110 580 V485 Q110 455 140 455 Z"
              fill="var(--bubble)" fill-opacity="0.93" stroke="var(--navy)" stroke-width="5" stroke-linejoin="round"/>
        <text x="248" y="553" text-anchor="middle" font-family="Delius, sans-serif" font-size="50" fill="var(--navy)">KNIRPS…</text>
      </g>
    </svg>

    <p class="subtitle-band">Raus aus der Panik und rein ins Vater werden<br>mit Verantwortung, Herz und Stil</p>
    <p class="author-name">Gernot Wallbrecht</p>
  </section>

</main>
</body>
</html>
```